KIVO 248
I need double sided standard sized Business Card [3.5" x 2"]
Open to designers choice
Modern
Pavel Rudakovsky
PO BOX 7132
Larkmont, OR 90318
pavel@tumq4.com
kivo248.com

```html
<!DOCTYPE html>
<html lang="en">
<head>
<meta charset="utf-8">
<title>KIVO 248 Business Cards</title>
<link href="https://fonts.googleapis.com/css2?family=Montserrat:wght@400;500;600&display=swap" rel="stylesheet">
<style>
  :root {
    --page-bg: #e7e4e0;
    --card-white: #fbfbfb;
    --card-frost: rgba(255,255,255,0.55);
    --brand-orange: #f0642c;
    --band-top: #f47a4c;
    --band-mid: #ea4e2a;
    --band-bottom: #cf3418;
    --silver-light: #f4f4f4;
    --silver-dark: #a9a9a9;
    --text-light: #ffffff;
    --frost-edge: rgba(255,255,255,0.85);
  }
  * { box-sizing: border-box; margin: 0; padding: 0; }
  html, body { width: 1200px; height: 730px; overflow: hidden; }
  body {
    background: var(--page-bg);
    font-family: "Montserrat", sans-serif;
    position: relative;
  }
  .card {
    position: absolute;
    width: 490px;
    height: 280px;
    border-radius: 16px;
    overflow: hidden;
    background: var(--card-white);
    box-shadow: 0 6px 18px rgba(0,0,0,0.18);
  }
  .card--frosted {
    background: var(--card-frost);
    border: 1px solid var(--frost-edge);
    box-shadow: 0 6px 18px rgba(0,0,0,0.10);
  }
  .pos-front-solid { left: 90px;  top: 60px; }
  .pos-front-clear { left: 620px; top: 60px; }
  .pos-back-solid  { left: 90px;  top: 390px; }
  .pos-back-clear  { left: 620px; top: 390px; }

  .brand {
    position: absolute;
    display: flex;
    align-items: center;
    gap: 14px;
  }
  .brand-mark {
    width: 46px; height: 46px;
    border-radius: 8px;
    background: var(--brand-orange);
  }
  .brand-name {
    font-weight: 600;
    font-size: 34px;
    color: var(--brand-orange);
    letter-spacing: 1px;
  }
  .card--front .brand { left: 110px; top: 30px; }
  .card--back .brand  { left: 130px; top: 70px; }
  .card--mirrored .brand { transform: scaleX(-1); }

  .silver-rule {
    position: absolute; left: 0; right: 0;
    height: 6px;
    background: linear-gradient(180deg, var(--silver-light), var(--silver-dark));
  }
  .band {
    position: absolute; left: 0; right: 0; bottom: 0;
    background: linear-gradient(180deg, var(--band-top), var(--band-mid) 45%, var(--band-bottom));
  }
  .card--frosted .band { opacity: 0.82; }
  .card--front .silver-rule { top: 108px; }
  .card--front .band { top: 114px; }
  .card--back .silver-rule { top: 158px; }
  .card--back .band { top: 164px; }

  .band-stripe {
    position: absolute; left: 0; right: 0; top: 52px;
    height: 3px;
    background: rgba(255,255,255,0.35);
  }
  .holder {
    position: absolute; left: 0; right: 0; top: 28px;
    text-align: center;
    color: var(--text-light);
    font-size: 11px;
    font-weight: 500;
    letter-spacing: 1px;
  }
  .contact {
    position: absolute; left: 0; right: 0; top: 78px;
    text-align: center;
    color: var(--text-light);
    font-size: 9.5px;
    letter-spacing: 0.6px;
  }
  .contact-row {
    display: flex;
    justify-content: center;
    gap: 12px;
    margin-top: 8px;
  }
  .contact-item { display: flex; align-items: center; gap: 4px; }
  .contact-item svg { width: 10px; height: 10px; }
  .web {
    position: absolute; left: 0; right: 0; top: 48px;
    text-align: center;
    color: var(--text-light);
    font-size: 10px;
    letter-spacing: 3px;
  }
  .card--mirrored .web { transform: scaleX(-1); }
</style>
</head>
<body>

<section class="card card--front pos-front-solid">
  <div class="brand"><span class="brand-mark"></span><span class="brand-name">KIVO 248</span></div>
  <div class="silver-rule"></div>
  <div class="band">
    <p class="holder">Pavel Rudakovsky | CEO</p>
    <div class="band-stripe"></div>
    <div class="contact">
      <p>PO BOX 7132 Larkmont, OR 90318</p>
      <div class="contact-row">
        <span class="contact-item"><svg viewBox="0 0 10 10"><path d="M2 1h2l1 2.5-1.3 1a5 5 0 0 0 1.8 1.8l1-1.3L9 6v2c0 .6-.5 1-1 1A7 7 0 0 1 1 2c0-.5.4-1 1-1z" fill="#fff"/></svg>470 555 0148</span>
        <span class="contact-item"><svg viewBox="0 0 10 10"><path d="M2 1h2l1 2.5-1.3 1a5 5 0 0 0 1.8 1.8l1-1.3L9 6v2c0 .6-.5 1-1 1A7 7 0 0 1 1 2c0-.5.4-1 1-1z" fill="#fff"/></svg>470 555 0193</span>
        <span class="contact-item"><svg viewBox="0 0 10 10"><path d="M2 1h2l1 2.5-1.3 1a5 5 0 0 0 1.8 1.8l1-1.3L9 6v2c0 .6-.5 1-1 1A7 7 0 0 1 1 2c0-.5.4-1 1-1z" fill="#fff"/></svg>470 555 0176</span>
      </div>
      <div class="contact-row">
        <span class="contact-item"><svg viewBox="0 0 10 10"><rect x="0.5" y="2" width="9" height="6" fill="none" stroke="#fff"/><path d="M0.5 2l4.5 3.5L9.5 2" fill="none" stroke="#fff"/></svg>pavel@tumq4.com</span>
        <span class="contact-item"><svg viewBox="0 0 10 10"><circle cx="5" cy="5" r="4.2" fill="none" stroke="#fff"/><path d="M1 5h8M5 1c-2 2.5-2 5.5 0 8M5 1c2 2.5 2 5.5 0 8" fill="none" stroke="#fff" stroke-width="0.8"/></svg>www.kivo248.com</span>
      </div>
    </div>
  </div>
</section>

<section class="card card--front card--frosted pos-front-clear">
  <div class="brand"><span class="brand-mark"></span><span class="brand-name">KIVO 248</span></div>
  <div class="silver-rule"></div>
  <div class="band">
    <p class="holder">Pavel Rudakovsky | CEO</p>
    <div class="band-stripe"></div>
    <div class="contact">
      <p>PO BOX 7132 Larkmont, OR 90318</p>
      <div class="contact-row">
        <span class="contact-item"><svg viewBox="0 0 10 10"><path d="M2 1h2l1 2.5-1.3 1a5 5 0 0 0 1.8 1.8l1-1.3L9 6v2c0 .6-.5 1-1 1A7 7 0 0 1 1 2c0-.5.4-1 1-1z" fill="#fff"/></svg>470 555 0148</span>
        <span class="contact-item"><svg viewBox="0 0 10 10"><path d="M2 1h2l1 2.5-1.3 1a5 5 0 0 0 1.8 1.8l1-1.3L9 6v2c0 .6-.5 1-1 1A7 7 0 0 1 1 2c0-.5.4-1 1-1z" fill="#fff"/></svg>470 555 0193</span>
        <span class="contact-item"><svg viewBox="0 0 10 10"><path d="M2 1h2l1 2.5-1.3 1a5 5 0 0 0 1.8 1.8l1-1.3L9 6v2c0 .6-.5 1-1 1A7 7 0 0 1 1 2c0-.5.4-1 1-1z" fill="#fff"/></svg>470 555 0176</span>
      </div>
      <div class="contact-row">
        <span class="contact-item"><svg viewBox="0 0 10 10"><rect x="0.5" y="2" width="9" height="6" fill="none" stroke="#fff"/><path d="M0.5 2l4.5 3.5L9.5 2" fill="none" stroke="#fff"/></svg>pavel@tumq4.com</span>
        <span class="contact-item"><svg viewBox="0 0 10 10"><circle cx="5" cy="5" r="4.2" fill="none" stroke="#fff"/><path d="M1 5h8M5 1c-2 2.5-2 5.5 0 8M5 1c2 2.5 2 5.5 0 8" fill="none" stroke="#fff" stroke-width="0.8"/></svg>www.kivo248.com</span>
      </div>
    </div>
  </div>
</section>

<section class="card card--back pos-back-solid">
  <div class="brand"><span class="brand-mark"></span><span class="brand-name">KIVO 248</span></div>
  <div class="silver-rule"></div>
  <div class="band">
    <p class="web">www.kivo248.com</p>
  </div>
</section>

<section class="card card--back card--frosted card--mirrored pos-back-clear">
  <div class="brand"><span class="brand-mark"></span><span class="brand-name">KIVO 248</span></div>
  <div class="silver-rule"></div>
  <div class="band">
    <p class="web">www.kivo248.com</p>
  </div>
</section>

</body>
</html>
```